Branding product image: TOMBEL (Golden Papaya) in Plastic Cup (Ready to Eat)

The product is sliced Fruit in Light syrup
Flavour: TOMBEL (Golden Papaya)
The temporary product name: TOMBEL
I want the product design to be something 'fun', 'natural', and 'colourful'
The design concept could be anything depends on your imagination, but it must be eye catchy and attractive.
Basically, I want you to be creative in designing the logo and the overall graphic design for the label.
The measurement is 20 cm (Length) x 6,5 cm (Height)
The target customers are young and health conscious audiences (10 years - 65 years old).
Create something different. Something extraordinary.
Brief summary about the fruit:
This fruit only grows in certain part of the world. It grows in mountain area that is in tropical climate. The fruit flesh has a yellowish-golden color. It has an extraordinary taste (unlike normal papaya) and it suits very well with any dishes from cold appetizer, white/ red meat, desserts, and cocktails.
I need a packaging design for Fruit Cup productThe product is sliced Fruit in Light syrup.There will be various flavours i.e. apple, lychee, peach, papaya, etc.However, you may design the product using one sample flavour (i.e. papaya) first, as the designs of other flavours could be adjusted afterwards.The temporary product name is: RICCANAI want the product design to be something 'fun', 'natural', and 'colourful'.The design concept could be anything depends on your imagination. Basically, I want you to be creative in designing the logo and the overall graphic design for the label. - Create something different. Something extraordinary -Additional:The measurement is 20cm (Length) x 5cm (Height).The target customers are young audiences (10 years - 35 years old).The product design must stand out in the supermarket shelf.It must be eye catchy and attractive.Thank you,Harold-PLEASE REFER TO DESIGN SAMPLE ATTACHED TO HAVE A BETTER UNDERSTANDING FOR THE PRODUCT CONCEPT- Added Wednesday, September 17, 2014
Project Deadline Extended Reason: Haven't found a good design. Added Friday, September 19, 2014
Project Deadline Extended Reason: Need more time for designers to finalize and perfect the design.Thank you,Harold Added Monday, September 29, 2014
Project Deadline Extended Reason: I haven't found a great design yet. Added Tuesday, February 24, 2015
Reason: Getting better designs now. Still Open to new ideas while refining the latest designs from some designers.
Please do your best in submitting other great designs!

```html
<!DOCTYPE html>
<html lang="en">
<head>
<meta charset="utf-8">
<title>LUPEDOS Sliced Fruit – Cup Label Family</title>
<link rel="stylesheet" href="https://fonts.googleapis.com/css2?family=Quicksand:wght@400;500;700&display=swap">
<style>
  :root {
    --canvas: #ffffff;
    --papaya: #ef5a2a;
    --papaya-light: #f4783c;
    --papaya-dark: #e03f27;
    --apple: #e8303a;
    --apple-light: #f04a55;
    --apple-dark: #c9212c;
    --peach: #f5a320;
    --peach-light: #f9bb45;
    --peach-dark: #ec8c12;
    --lychee: #e0305a;
    --lychee-light: #ec5078;
    --lychee-dark: #c21f4c;
    --brand-red: #e52a2f;
    --brand-green: #3db549;
    --label-text: #ffffff;
    --tint-up: rgba(255, 255, 255, 0.10);
    --tint-down: rgba(120, 0, 20, 0.12);
  }
  * { box-sizing: border-box; margin: 0; padding: 0; }
  html, body { width: 1200px; height: 1000px; overflow: hidden; }
  body {
    position: relative;
    background: var(--canvas);
    font-family: "Quicksand", "Helvetica Neue", Arial, sans-serif;
  }

  /* ---------- shared label art: tonal bands over a fruit-coloured field ---------- */
  .label__art { position: absolute; inset: 0; }
  .art {
    background-image:
      linear-gradient(118deg, transparent 0 18%, var(--tint-up) 18% 31%, transparent 31% 100%),
      linear-gradient(62deg, transparent 0 42%, var(--tint-down) 42% 55%, transparent 55% 100%),
      linear-gradient(140deg, transparent 0 64%, var(--tint-up) 64% 76%, transparent 76% 100%),
      linear-gradient(35deg, transparent 0 80%, var(--tint-down) 80% 90%, transparent 90% 100%),
      radial-gradient(circle at 20% 30%, var(--tint-up), transparent 40%),
      radial-gradient(circle at 80% 70%, var(--tint-down), transparent 45%),
      linear-gradient(135deg, var(--c-light), var(--c-mid) 50%, var(--c-dark));
  }
  .art--papaya { --c-light: var(--papaya-light); --c-mid: var(--papaya); --c-dark: var(--papaya-dark); }
  .art--apple  { --c-light: var(--apple-light);  --c-mid: var(--apple);  --c-dark: var(--apple-dark); }
  .art--peach  { --c-light: var(--peach-light);  --c-mid: var(--peach);  --c-dark: var(--peach-dark); }
  .art--lychee { --c-light: var(--lychee-light); --c-mid: var(--lychee); --c-dark: var(--lychee-dark); }

  /* ---------- label text block ---------- */
  .label__info {
    position: absolute;
    top: 0; bottom: 0;
    display: flex;
    flex-direction: column;
    align-items: center;
    justify-content: center;
    color: var(--label-text);
    text-align: center;
    line-height: 1;
    white-space: nowrap;
  }
  .label__brand  { font-weight: 700; font-size: 2.1em; letter-spacing: 0.02em; margin-bottom: 0.45em; }
  .label__sliced { font-weight: 500; font-size: 0.95em; letter-spacing: 0.02em; }
  .label__fruit  { font-weight: 700; font-size: 1.75em; letter-spacing: 0.06em; margin-bottom: 0.3em; }
  .label__icon   { width: 0.8em; height: 0.95em; border-radius: 50%; background: var(--label-text); margin-bottom: 0.6em; }
  .label__syrup  { font-weight: 400; font-size: 1em; letter-spacing: 0.03em; margin-bottom: 1.1em; }
  .label__weight { font-weight: 700; font-size: 0.45em; letter-spacing: 0.02em; }

  /* ---------- flat wrap labels ---------- */
  .label { position: absolute; overflow: hidden; }
  .label--papaya { left: -20px; top: 40px; width: 910px; height: 228px; transform: rotate(-4.5deg); font-size: 22px; }
  .label--papaya .label__info { left: 290px; width: 230px; }

  .label--apple  { left: -20px; top: 295px; width: 550px; height: 132px; transform: rotate(-4.5deg); font-size: 12.5px; }
  .label--peach  { left: -20px; top: 445px; width: 540px; height: 132px; transform: rotate(-4.5deg); font-size: 12.5px; }
  .label--lychee { left: -20px; top: 597px; width: 525px; height: 132px; transform: rotate(-4.5deg); font-size: 12.5px; }
  .label--apple .label__info  { left: 190px; width: 140px; }
  .label--peach .label__info  { left: 180px; width: 140px; }
  .label--lychee .label__info { left: 165px; width: 140px; }

  /* ---------- brand lockup ---------- */
  .brand-lockup {
    position: absolute;
    left: 600px; top: 385px;
    width: 500px;
    display: flex;
    flex-direction: column;
    align-items: flex-end;
  }
  .brand-lockup__row { display: flex; align-items: center; gap: 14px; }
  .brand-lockup__name {
    font-weight: 700;
    font-size: 84px;
    letter-spacing: 0.02em;
    color: var(--brand-red);
    line-height: 1;
  }
  .brand-lockup__mark { width: 22px; height: 22px; border-radius: 50%; background: var(--brand-green); }
  .brand-lockup__tagline {
    margin-top: 22px;
    font-weight: 500;
    font-size: 26px;
    letter-spacing: 0.02em;
    color: var(--brand-green);
  }

  /* ---------- cup front panels, shown flat ---------- */
  .cup-front { position: absolute; overflow: hidden; border-radius: 6px; }
  .cup-front .label__info { left: 0; right: 0; }
  .cup-front--apple  { left: 122px; top: 790px; width: 170px; height: 160px; font-size: 11.5px; }
  .cup-front--peach  { left: 380px; top: 790px; width: 170px; height: 160px; font-size: 11.5px; }
  .cup-front--papaya { left: 615px; top: 690px; width: 300px; height: 270px; font-size: 19px; }
  .cup-front--lychee { left: 960px; top: 790px; width: 170px; height: 160px; font-size: 11.5px; }
</style>
</head>
<body>

  <section class="label label--papaya">
    <div class="label__art art art--papaya" role="img" aria-label="Scattered papaya silhouettes over faceted orange shapes"></div>
    <div class="label__info">
      <p class="label__brand">LUPEDOS</p>
      <p class="label__sliced">SLICED</p>
      <p class="label__fruit">PAPAYA</p>
      <span class="label__icon" role="img" aria-label="Small papaya icon"></span>
      <p class="label__syrup">in LIGHT SYRUP</p>
      <p class="label__weight">NET WT 6 OZ (170G)</p>
    </div>
  </section>

  <section class="label label--apple">
    <div class="label__art art art--apple" role="img" aria-label="Scattered apple silhouettes over faceted red shapes"></div>
    <div class="label__info">
      <p class="label__brand">LUPEDOS</p>
      <p class="label__sliced">SLICED</p>
      <p class="label__fruit">APPLE</p>
      <span class="label__icon" role="img" aria-label="Small apple icon"></span>
      <p class="label__syrup">in LIGHT SYRUP</p>
      <p class="label__weight">NET WT 6 OZ (170G)</p>
    </div>
  </section>

  <section class="label label--peach">
    <div class="label__art art art--peach" role="img" aria-label="Scattered peach half slices over faceted amber shapes"></div>
    <div class="label__info">
      <p class="label__brand">LUPEDOS</p>
      <p class="label__sliced">SLICED</p>
      <p class="label__fruit">PEACH</p>
      <span class="label__icon" role="img" aria-label="Small peach icon"></span>
      <p class="label__syrup">in LIGHT SYRUP</p>
      <p class="label__weight">NET WT 6 OZ (170G)</p>
    </div>
  </section>

  <section class="label label--lychee">
    <div class="label__art art art--lychee" role="img" aria-label="Scattered lychee silhouettes over faceted crimson shapes"></div>
    <div class="label__info">
      <p class="label__brand">LUPEDOS</p>
      <p class="label__sliced">SLICED</p>
      <p class="label__fruit">LYCHEE</p>
      <span class="label__icon" role="img" aria-label="Small lychee icon"></span>
      <p class="label__syrup">in LIGHT SYRUP</p>
      <p class="label__weight">NET WT 6 OZ (170G)</p>
    </div>
  </section>

  <div class="brand-lockup">
    <div class="brand-lockup__row">
      <span class="brand-lockup__name">LUPEDOS</span>
      <span class="brand-lockup__mark"></span>
    </div>
    <p class="brand-lockup__tagline">SLICED FRUIT</p>
  </div>

  <section class="cup-front cup-front--apple">
    <div class="label__art art art--apple" role="img" aria-label="Apple pattern on red cup front"></div>
    <div class="label__info">
      <p class="label__brand">LUPEDOS</p>
      <p class="label__sliced">SLICED</p>
      <p class="label__fruit">APPLE</p>
      <span class="label__icon" role="img" aria-label="Small apple icon"></span>
      <p class="label__syrup">in LIGHT SYRUP</p>
      <p class="label__weight">NET WT 6 OZ (170G)</p>
    </div>
  </section>

  <section class="cup-front cup-front--peach">
    <div class="label__art art art--peach" role="img" aria-label="Peach slice pattern on amber cup front"></div>
    <div class="label__info">
      <p class="label__brand">LUPEDOS</p>
      <p class="label__sliced">SLICED</p>
      <p class="label__fruit">PEACH</p>
      <span class="label__icon" role="img" aria-label="Small peach icon"></span>
      <p class="label__syrup">in LIGHT SYRUP</p>
      <p class="label__weight">NET WT 6 OZ (170G)</p>
    </div>
  </section>

  <section class="cup-front cup-front--papaya">
    <div class="label__art art art--papaya" role="img" aria-label="Papaya pattern on orange cup front"></div>
    <div class="label__info">
      <p class="label__brand">LUPEDOS</p>
      <p class="label__sliced">SLICED</p>
      <p class="label__fruit">PAPAYA</p>
      <span class="label__icon" role="img" aria-label="Small papaya icon"></span>
      <p class="label__syrup">in LIGHT SYRUP</p>
      <p class="label__weight">NET WT 6 OZ (170G)</p>
    </div>
  </section>

  <section class="cup-front cup-front--lychee">
    <div class="label__art art art--lychee" role="img" aria-label="Lychee pattern on crimson cup front"></div>
    <div class="label__info">
      <p class="label__brand">LUPEDOS</p>
      <p class="label__sliced">SLICED</p>
      <p class="label__fruit">LYCHEE</p>
      <span class="label__icon" role="img" aria-label="Small lychee icon"></span>
      <p class="label__syrup">in LIGHT SYRUP</p>
      <p class="label__weight">NET WT 6 OZ (170G)</p>
    </div>
  </section>

</body>
</html>
```